Food Packaging Design Project

We already have an established brand but feel that our packaging could be stronger. We would like the same logo outline , colour scheme and wording on the front and back... so that it is still recognisable to our customers but just a little more professional looking with the wow factor to help it stand out on the shelve.

We need both front and back design with colours on the back also.

The design must contain our registered logo design but can be added to.

The back doesn't have to be split into 2 columns as in the image provided.

The packets arn't the same as the old packs (as in picture attached) but instead will be pouches with solid edges.

We will need working files so that we can amend ourselves once the final design has been chosen.

Thanks in advance!
Updates

Project Deadline Extended
Reason: havent quite got what we are after, not enough designs submitted.

Requirements
Must have
• The design must contain our registered logo... see image attached.

Must contain our colour that we currently have.

Must have the same writing on the front and back.

```html
<!DOCTYPE html>
<html lang="en">
<head>
<meta charset="utf-8">
<title>Slim Strands – Pouch Front</title>
<link rel="stylesheet" href="https://fonts.googleapis.com/css2?family=Fira+Sans:wght@600;700&family=Delius&display=swap">
<style>
  :root {
    --backdrop: #e8e2cf;
    --pouch-white: #ffffff;
    --leaf-green: #839a3c;
    --label-red: #c0202a;
    --peach: #f8c06a;
    --edge-shadow: rgba(190, 70, 40, 0.45);
  }
  html, body {
    margin: 0;
    width: 1200px;
    height: 1000px;
    overflow: hidden;
    background: var(--backdrop);
  }
  .canvas { display: block; width: 1200px; height: 1000px; }
  .pouch { fill: var(--pouch-white); filter: drop-shadow(0 0 6px var(--edge-shadow)); }
  .stripe, .hero-disc, .badge-core, .bowl-art { fill: var(--leaf-green); }
  .hero-ring, .footer-panel { fill: var(--pouch-white); }
  .brand-plate, .flavour-band { fill: var(--label-red); }
  .brand-plate { filter: drop-shadow(2px 4px 4px rgba(0,0,0,0.3)); }
  .brand-name {
    font-family: "Fira Sans", sans-serif; font-weight: 700; font-size: 58px;
    fill: var(--pouch-white);
  }
  .tagline-pill { fill: var(--pouch-white); }
  .tagline {
    font-family: "Delius", sans-serif; font-size: 20px; fill: var(--label-red);
  }
  .badge-ring { fill: var(--pouch-white); filter: drop-shadow(2px 3px 3px rgba(0,0,0,0.35)); }
  .badge-text {
    font-family: "Fira Sans", sans-serif; font-weight: 600; font-size: 21px;
    fill: var(--pouch-white);
  }
  .claim-core { fill: var(--peach); }
  .claim-text {
    font-family: "Fira Sans", sans-serif; font-weight: 600; font-size: 20px;
    fill: var(--label-red);
  }
  .flavour-name {
    font-family: "Fira Sans", sans-serif; font-weight: 700; font-size: 34px;
    letter-spacing: 5px; fill: var(--pouch-white);
  }
  .free-from {
    font-family: "Fira Sans", sans-serif; font-weight: 600; font-size: 28px;
    fill: var(--label-red);
  }
</style>
</head>
<body>
<svg class="canvas" viewBox="0 0 1200 1000" xmlns="http://www.w3.org/2000/svg">
  <defs>
    <clipPath id="pouch-clip"><rect x="275" y="42" width="650" height="920"/></clipPath>
  </defs>

  <rect class="pouch" x="275" y="42" width="650" height="920"/>

  <g class="stripes" clip-path="url(#pouch-clip)">
    <rect class="stripe" x="305" y="75" width="38" height="862" rx="19"/>
    <rect class="stripe" x="383" y="75" width="38" height="862" rx="19"/>
    <rect class="stripe" x="461" y="75" width="38" height="862" rx="19"/>
    <rect class="stripe" x="539" y="75" width="38" height="862" rx="19"/>
    <rect class="stripe" x="617" y="75" width="38" height="862" rx="19"/>
    <rect class="stripe" x="695" y="75" width="38" height="862" rx="19"/>
    <rect class="stripe" x="773" y="75" width="38" height="862" rx="19"/>
    <rect class="stripe" x="851" y="75" width="38" height="862" rx="19"/>
  </g>

  <rect class="footer-panel" x="430" y="880" width="340" height="70"/>

  <g class="hero" clip-path="url(#pouch-clip)">
    <circle class="hero-disc" cx="600" cy="380" r="292"/>
    <circle class="hero-ring" cx="575" cy="335" r="212"/>
    <circle class="bowl-art" cx="575" cy="335" r="198" role="img" aria-label="Illustration of a steaming bowl of noodles"/>
  </g>

  <g class="claims">
    <circle class="badge-ring" cx="815" cy="148" r="64"/>
    <circle class="claim-core" cx="815" cy="148" r="57"/>
    <text class="claim-text" x="815" y="146" text-anchor="middle">8 Calories</text>
    <text class="claim-text" x="815" y="170" text-anchor="middle">Per Pack</text>

    <circle class="badge-ring" cx="835" cy="272" r="50"/>
    <circle class="claim-core" cx="835" cy="272" r="44"/>
    <text class="claim-text" x="835" y="279" text-anchor="middle">Organic</text>
  </g>

  <g class="brand" transform="rotate(-5 600 530)">
    <rect class="brand-plate" x="355" y="455" width="495" height="165" rx="14"/>
    <text class="brand-name" x="600" y="532" text-anchor="middle">Slim Strands</text>
    <rect class="tagline-pill" x="395" y="552" width="420" height="40" rx="20"/>
    <text class="tagline" x="605" y="579" text-anchor="middle">The Alternative To Pasta For Weight Loss</text>
  </g>

  <g class="zero-badges">
    <circle class="badge-ring" cx="388" cy="738" r="59"/>
    <circle class="badge-core" cx="388" cy="738" r="51"/>
    <text class="badge-text" x="388" y="733" text-anchor="middle">Zero</text>
    <text class="badge-text" x="388" y="758" text-anchor="middle">Net Cals</text>

    <circle class="badge-ring" cx="528" cy="738" r="59"/>
    <circle class="badge-core" cx="528" cy="738" r="51"/>
    <text class="badge-text" x="528" y="733" text-anchor="middle">Zero</text>
    <text class="badge-text" x="528" y="758" text-anchor="middle">Sugar</text>

    <circle class="badge-ring" cx="668" cy="738" r="59"/>
    <circle class="badge-core" cx="668" cy="738" r="51"/>
    <text class="badge-text" x="668" y="733" text-anchor="middle">Zero</text>
    <text class="badge-text" x="668" y="758" text-anchor="middle">Salt</text>

    <circle class="badge-ring" cx="808" cy="738" r="59"/>
    <circle class="badge-core" cx="808" cy="738" r="51"/>
    <text class="badge-text" x="808" y="733" text-anchor="middle">Zero</text>
    <text class="badge-text" x="808" y="758" text-anchor="middle">Glutten</text>
  </g>

  <g class="flavour">
    <path class="flavour-band" d="M458 822 Q600 810 742 822 L748 868 Q600 858 452 870 Z"/>
    <text class="flavour-name" x="600" y="856" text-anchor="middle">ORIGINAL</text>
  </g>

  <text class="free-from" x="600" y="922" text-anchor="middle">Fat Free . Wheat Free</text>
</svg>
</body>
</html>
```